Business Card Design for Kidvale (Hires out childrens play areas)

Looking to have a business card designed for a company we just bought. The company rents out childrens play areas.

I have uploaded a couple of examples of the kind of business card style I like. Here are two more examples:

https://quorvastudio.nz/project/bright-romp-branding/
https://imgvaultcdn.com/design_img/8841052/302917/302917_5518203_8841052_b73e19a2_image.jpg

I think a white card will be best due to all the colours in the logo.

Size we require: 3.75" x 2.25" (horizontally orientated) with a 0.125" bleed

Uploaded is two versions of our logo.

Details for the card:
1. My name: Liam Verster
2. Title: Managing Director
3. Phone no: 021 563 417
4. Email: liam@kidvale.co.nz
5. URL: www.kidvale.co.nz
6. Address:
PO Box 318625
Fernlea, Auckland

Let me know if you need anything else.

Target Market(s)

Hospitals, doctors surgeries, bed shops, etc.

Contact Information for Business Card

Details for the card:
1. My name: Liam Verster
3. Phone no: 021 563 417
5. URL: www.kidvale.co.nz
6. Address:
PO Box 318625
Fernlea, Auckland

Requirements
Should not have
• Not too busy.

```html
<!DOCTYPE html>
<html lang="en">
<head>
<meta charset="utf-8">
<title>Kidvale – Business Card</title>
<link rel="stylesheet" href="https://fonts.googleapis.com/css2?family=Open+Sans:wght@400;700&display=swap">
<style>
  :root {
    --backdrop: #2b2b2d;
    --card: #f5f5f6;
    --brand-blue: #0f55a3;
    --ink: #1b1b1b;
    --accent-orange: #f08a1c;
    --white: #ffffff;
    --faded-violet: #d9cfe6;
    --faded-pink: #ecd6e0;
  }
  * { margin: 0; padding: 0; box-sizing: border-box; }
  html, body {
    width: 1200px; height: 923px; overflow: hidden;
    background: var(--backdrop);
    font-family: "Open Sans", Arial, sans-serif;
  }
  .canvas {
    width: 1200px; height: 923px;
    display: flex; flex-direction: column; align-items: center; justify-content: center;
    gap: 40px;
  }
  .card {
    position: relative;
    width: 600px; height: 360px;
    background: var(--card);
    overflow: hidden;
  }

  /* blue band with inner white rule */
  .band {
    position: absolute; top: 0; bottom: 0; width: 66px;
    background: var(--brand-blue);
  }
  .band::after {
    content: ""; position: absolute; top: 0; bottom: 0; width: 3px; background: var(--white);
  }
  .card-front .band { left: 0; }
  .card-front .band::after { left: 52px; }
  .card-back .band { right: 0; }
  .card-back .band::after { right: 52px; }

  /* brand name straddling the band edge */
  .brand {
    position: absolute;
    display: flex; align-items: center; gap: 10px;
    background: var(--white);
    padding: 10px 18px 10px 14px;
    border-radius: 14px;
  }
  .brand-dot {
    width: 20px; height: 20px; border-radius: 50%;
    background: var(--accent-orange);
  }
  .brand-name {
    font-size: 38px; font-weight: 700; color: var(--accent-orange); line-height: 1;
  }
  .card-front .brand { left: 30px; top: 140px; }
  .card-back .brand { right: 20px; top: 40px; }

  /* front: identity & contacts */
  .identity {
    position: absolute; right: 40px; top: 46px; text-align: right;
  }
  .identity-name {
    font-size: 32px; font-weight: 400; color: var(--brand-blue); line-height: 1.05;
  }
  .identity-title {
    font-size: 14px; font-weight: 400; color: var(--ink); margin-top: 1px;
  }
  .contact {
    position: absolute; right: 40px; top: 180px;
    list-style: none; text-align: right;
  }
  .contact-item {
    display: flex; justify-content: flex-end; align-items: center; gap: 8px;
    font-size: 14px; color: var(--ink); line-height: 22px;
  }
  .contact-item svg { width: 12px; height: 12px; fill: var(--brand-blue); flex: none; }
  .contact-item .gap { display: inline-block; width: 10px; }

  /* back: faded illustration area */
  .back-illustration {
    position: absolute; left: 20px; top: 70px;
    width: 330px; height: 300px; border-radius: 50% 50% 0 0;
    background: radial-gradient(circle at 50% 45%, var(--faded-pink) 0%, var(--faded-violet) 70%);
    opacity: 0.8;
  }
</style>
</head>
<body>
<div class="canvas">
  <section class="card card-back">
    <div class="back-illustration" role="img" aria-label="Large faded mascot illustration in soft violet and pink"></div>
    <div class="band"></div>
    <div class="brand">
      <span class="brand-dot"></span>
      <span class="brand-name">Kidvale</span>
    </div>
  </section>

  <section class="card card-front">
    <div class="band"></div>
    <div class="brand">
      <span class="brand-dot"></span>
      <span class="brand-name">Kidvale</span>
    </div>

    <header class="identity">
      <h1 class="identity-name">Liam Verster</h1>
      <p class="identity-title">Managing Director</p>
    </header>

    <ul class="contact">
      <li class="contact-item">021 563 417
        <svg viewBox="0 0 24 24"><path d="M6.6 10.8a15.1 15.1 0 0 0 6.6 6.6l2.2-2.2a1 1 0 0 1 1-.25 11.4 11.4 0 0 0 3.6.57 1 1 0 0 1 1 1V20a1 1 0 0 1-1 1A17 17 0 0 1 3 4a1 1 0 0 1 1-1h3.5a1 1 0 0 1 1 1 11.4 11.4 0 0 0 .57 3.6 1 1 0 0 1-.25 1z"/></svg>
      </li>
      <li class="contact-item">liam@kidvale.co.nz
        <svg viewBox="0 0 24 24"><path d="M2 5h20v14H2zm2 2v.5l8 5 8-5V7zm0 2.8V17h16V9.8l-8 5z"/></svg>
      </li>
      <li class="contact-item">www.kidvale.co.nz
        <svg viewBox="0 0 24 24"><path d="M12 2a10 10 0 1 0 0 20 10 10 0 0 0 0-20zm6.9 9h-3a15 15 0 0 0-1.2-5.6A8 8 0 0 1 18.9 11zM12 4.1c.9 1.2 1.7 3.5 1.9 6.9h-3.8c.2-3.4 1-5.7 1.9-6.9zM9.3 5.4A15 15 0 0 0 8.1 11h-3a8 8 0 0 1 4.2-5.6zM5.1 13h3a15 15 0 0 0 1.2 5.6A8 8 0 0 1 5.1 13zm6.9 6.9c-.9-1.2-1.7-3.5-1.900-6.9h3.8c-.2 3.4-1 5.7-1.9 6.9zm2.7-1.3a15 15 0 0 0 1.2-5.6h3a8 8 0 0 1-4.2 5.6z"/></svg>
      </li>
      <li class="contact-item">PO Box 318625<span class="gap"></span>Fernlea, Auckland
        <svg viewBox="0 0 24 24"><path d="M12 2a7 7 0 0 0-7 7c0 5.2 7 13 7 13s7-7.8 7-13a7 7 0 0 0-7-7zm0 9.5A2.5 2.5 0 1 1 12 6.5a2.5 2.5 0 0 1 0 5z"/></svg>
      </li>
    </ul>
  </section>
</div>
</body>
</html>
```